Barrister in Western Australia needs a fully custom logo, stationery and fonts

Barrister based in Western Australia seeking a fully custom logo, electronic and hardcopy stationery set (including email signature, document headers and footers for use with retainer agreement, invoices, letters of advice etc), custom fonts and business card design. Certain non-optional wording regarding liability limitation has to appear on documents (wording will be supplied but is on the uploaded examples). Have used this platform previously and have outgrown the previous design - samples of which are attached. I live very close to, and spend a significant amount time when not working in or around, the ocean. Use of colours or designs representative of that would be appreciated. The final design should try and communicate strength (of representation), the ability to be flexible (for example, settlements) and the fact I make myself accessible to clients - all factors shown in water/ocean.

Target Market(s)

Legal services providers, solicitors

Industry/Entity Type

Legal

Font styles to use
Serif
Decorative

Requirements
Must have
• Certain insurance wording regarding limitation of liability. Progressive feel to the set including a custom font for use in Office 365. Logo or design that is progressive - can relate to the ocean, water or waves (representing an ability to be fluid, dynamic but inheerent strength)
Nice to have
• Colour
Should not have
• Traditional calligraphy or legal fonts or feel - should not contain any traditional legal industry designs such as pens, scales of justice etc.

```html
<!DOCTYPE html>
<html lang="en">
<head>
<meta charset="utf-8">
<title>Daniel R Whitford – Letterhead</title>
<link rel="stylesheet" href="https://fonts.googleapis.com/css2?family=Montserrat:wght@400;500&display=swap">
<style>
  :root {
    --navy: #081c36;
    --teal-light: #3690b0;
    --teal-dark: #2c7aa6;
    --mist: #d4d8da;
    --paper: #ffffff;
    --ink: #111111;
  }
  * { margin: 0; padding: 0; box-sizing: border-box; }
  html, body {
    width: 849px;
    height: 1200px;
    overflow: hidden;
    background: var(--paper);
  }
  .letterhead {
    position: relative;
    width: 849px;
    height: 1200px;
    font-family: "Montserrat", sans-serif;
    color: var(--ink);
    overflow: hidden;
  }
  .waves {
    position: absolute;
    inset: 0;
    width: 849px;
    height: 1200px;
  }
  .brand-name {
    position: absolute;
    left: 62px;
    top: 100px;
    width: 190px;
    text-align: center;
    font-size: 19px;
    font-weight: 500;
    color: var(--paper);
    letter-spacing: 0.2px;
  }
  .contact {
    position: absolute;
    left: 543px;
    top: 58px;
    display: grid;
    grid-template-columns: 33px auto;
    row-gap: 5px;
    font-size: 15.5px;
    font-weight: 400;
    color: var(--paper);
    line-height: 20px;
  }
  .contact .value { white-space: nowrap; }
  .contact .address { line-height: 20px; }
  .footer-rule {
    position: absolute;
    left: 65px;
    top: 1003px;
    width: 179px;
    height: 5px;
    background: var(--mist);
  }
  .disclaimer {
    position: absolute;
    left: 65px;
    top: 1018px;
    width: 790px;
    font-size: 14.6px;
    line-height: 18px;
    font-weight: 400;
    color: var(--ink);
  }
</style>
</head>
<body>
  <main class="letterhead">
    <svg class="waves" viewBox="0 0 1624 2296" preserveAspectRatio="none" aria-hidden="true">
      <defs>
        <linearGradient id="tealSweep" x1="0" y1="0" x2="1" y2="0">
          <stop offset="0" stop-color="var(--teal-light)"/>
          <stop offset="1" stop-color="var(--teal-dark)"/>
        </linearGradient>
      </defs>
      <path class="header-mist" fill="var(--mist)"
            d="M540,0 H1624 V472 C1520,482 1430,480 1360,472 C1080,440 880,302 540,298 Z"/>
      <path class="header-sea" fill="url(#tealSweep)"
            d="M560,0 H1624 V398 C1520,414 1420,414 1360,408 C1080,378 880,282 570,275 Z"/>
      <path class="header-deep" fill="var(--navy)"
            d="M0,0 H1070 C860,80 700,170 580,278 C430,410 280,450 0,465 Z"/>
      <path class="footer-sea" fill="url(#tealSweep)"
            d="M100,2202 C700,2196 1200,2172 1624,2130 V2220 H0 Z"/>
      <path class="footer-deep" fill="var(--navy)"
            d="M0,2202 H200 C800,2200 1300,2190 1624,2165 V2296 H0 Z"/>
    </svg>

    <div class="brand-name">Daniel R Whitford</div>

    <div class="contact">
      <span class="label">m.</span><span class="value">+61 (0) 400 555 218</span>
      <span class="label">t.</span><span class="value">+61 8 9000 3127</span>
      <span class="label">a.</span><span class="value address">Level 9, 40 Harbourview<br>Parade, Perth, WA, 6000</span>
    </div>

    <div class="footer-rule"></div>
    <p class="disclaimer">
      Disclaimer: Liability limited by a scheme approved under proffesional standard legislation.<br>
      This email (including any attachments) is confidential and may be privileged. it may be read,<br>
      copied and used only by the intended recipent. iIf you have recieved it in error, please contact<br>
      the sender immediately by return email. please then delete both email and do not disclose<br>
      their contents to any person
    </p>
  </main>
</body>
</html>
```